Accounting Practice Business Card Design

I have a logo I am happy for you to use in the design of the Business Card.
You can edit and change colours as you please, I am not fixated on it.
I am looking for a modern and clean overall feel for the finished design.

The business is a small accounting practice who thrives on word of mouth referrals and this card will be given to all current and prospect clients.

Industry/Entity Type

Accountant

Contact Information for Business Card

Marcus Vell
Level 5, 8 Ashcombe Ridge Road
FERNMOOR RISE VIC 3187
Phone: 9481 3052
Email: mvell@qrnaccountants.com.au
Web: www.qrnaccountants.com.au

Font styles to use
Serif
Sans Serif

Colors
0555a3
3277b5
85acd3
0393ce
33a6d7
85cae6
00a990
33b8a4
9bcb3c

Requirements
Must have
• "The end to your tax problems begin with us"
• "A referral from you is our greatest compliment"
Nice to have
• Modern clean professional

```html
<!DOCTYPE html>
<html lang="en">
<head>
<meta charset="utf-8">
<title>QRN Accountants – Business Card</title>
<link href="https://fonts.googleapis.com/css2?family=Work+Sans:wght@400;600&display=swap" rel="stylesheet">
<style>
  :root {
    --backdrop: #141415;
    --card: #1d1d1f;
    --text-dim: #55555a;
    --text-faint: #3e3e42;
    --silver: #d9d9dc;
    --silver-soft: #b9b9bd;
    --brand-deep: #0555a3;
    --brand-blue: #0393ce;
    --brand-sky: #85cae6;
    --brand-teal: #00a990;
  }
  * { margin: 0; padding: 0; box-sizing: border-box; }
  html, body {
    width: 1200px; height: 900px; overflow: hidden;
    background: var(--backdrop);
    font-family: "Work Sans", Arial, sans-serif;
  }
  .canvas {
    width: 1200px; height: 900px;
    display: flex; flex-direction: column; align-items: center; justify-content: center;
    gap: 46px;
  }
  .card {
    position: relative;
    width: 680px; height: 389px;
    background: var(--card);
    border-radius: 2px;
    box-shadow: 0 10px 30px rgba(0,0,0,.5);
    overflow: hidden;
  }
  .card::after {
    content: ""; position: absolute; left: 0; right: 0; bottom: 0; height: 4px;
    background: linear-gradient(90deg, var(--brand-deep), var(--brand-blue), var(--brand-teal));
  }

  /* Brand name placeholder: one colour, one weight, one size */
  .brand-name {
    display: inline-flex; align-items: center; gap: 12px;
    font-weight: 600; color: var(--brand-sky);
    text-transform: uppercase; letter-spacing: 0.06em; white-space: nowrap;
  }
  .brand-mark { display: inline-block; background: var(--brand-blue); flex: none; }

  /* Front */
  .card-front {
    display: flex; flex-direction: column; align-items: center; justify-content: center;
    text-align: center;
  }
  .card-front .brand-name { font-size: 40px; }
  .card-front .brand-mark { width: 28px; height: 28px; }
  .referral-note {
    margin-top: 26px;
    color: var(--text-dim);
    font-size: 19px; line-height: 1.3; letter-spacing: 0.04em;
  }
  .referral-note .thanks { display: block; margin-top: 4px; }
  .front-signoff {
    margin-top: 14px;
    color: var(--text-dim);
    font-size: 13px; letter-spacing: 0.06em; text-transform: uppercase;
  }

  /* Back */
  .back-tagline {
    position: absolute; top: 30px; left: 0; right: 0;
    text-align: center; color: var(--text-faint);
    font-size: 16px; line-height: 1.25; letter-spacing: 0.05em;
  }
  .back-tagline .tagline-brand { display: block; text-transform: uppercase; }
  .back-body {
    position: absolute; top: 132px; left: 44px; right: 36px;
    display: flex; align-items: stretch;
  }
  .back-logo { width: 290px; display: flex; align-items: center; }
  .back-logo .brand-name { font-size: 24px; gap: 10px; }
  .back-logo .brand-mark { width: 18px; height: 18px; }
  .divider { width: 1px; background: var(--brand-deep); margin: 0 26px 0 4px; }
  .contact { color: var(--silver-soft); padding: 6px 0; }
  .person-name {
    font-size: 26px; color: var(--silver);
    text-transform: uppercase; letter-spacing: 0.08em; font-weight: 400;
  }
  .person-role { font-size: 15px; color: var(--brand-sky); letter-spacing: 0.05em; margin-bottom: 14px; }
  .address { font-size: 15px; line-height: 1.3; letter-spacing: 0.06em; margin-bottom: 10px; }
  .contact-list { list-style: none; font-size: 15px; letter-spacing: 0.05em; line-height: 1.35; }
  .contact-list li { display: flex; align-items: center; gap: 10px; }
  .contact-list svg { width: 11px; height: 11px; flex: none; }
</style>
</head>
<body>
<main class="canvas">

  <section class="card card-front" aria-label="Card front">
    <div class="brand-name"><span class="brand-mark"></span>QRN Accountants</div>
    <p class="referral-note">
      A referral from you is our<br>greatest compliment.
      <span class="thanks">Thank you for choosing us.</span>
    </p>
    <p class="front-signoff">QRN Accountants</p>
  </section>

  <section class="card card-back" aria-label="Card back">
    <p class="back-tagline">
      <span class="tagline-brand">QRN Accountants</span>
      The end to your tax problems begin with us.
    </p>
    <div class="back-body">
      <div class="back-logo">
        <div class="brand-name"><span class="brand-mark"></span>QRN Accountants</div>
      </div>
      <div class="divider"></div>
      <div class="contact">
        <h1 class="person-name">Marcus Vell</h1>
        <p class="person-role">Accountant</p>
        <p class="address">Level 5, 8 Ashcombe Ridge Road<br>FERNMOOR RISE VIC 3187</p>
        <ul class="contact-list">
          <li>
            <svg viewBox="0 0 12 12" aria-hidden="true"><path d="M2.5 1 L4.5 1 L5 3.5 L3.8 4.4 Q4.8 6.8 7.6 8.2 L8.5 7 L11 7.5 L11 9.5 Q10.5 11 9 11 Q1 10 1 2.5 Q1 1 2.5 1Z" fill="#33a6d7"/></svg>
            9481 3052
          </li>
          <li>
            <svg viewBox="0 0 12 12" aria-hidden="true"><rect x="1" y="2.5" width="10" height="7" fill="none" stroke="#33a6d7" stroke-width="1.2"/><path d="M1 2.5 L6 6.5 L11 2.5" fill="none" stroke="#33a6d7" stroke-width="1.2"/></svg>
            mvell@qrnaccountants.com.au
          </li>
          <li>
            <svg viewBox="0 0 12 12" aria-hidden="true"><circle cx="6" cy="6" r="5" fill="none" stroke="#33a6d7" stroke-width="1.1"/><ellipse cx="6" cy="6" rx="2.2" ry="5" fill="none" stroke="#33a6d7" stroke-width="1"/><path d="M1 6 H11" stroke="#33a6d7" stroke-width="1"/></svg>
            www.qrnaccountants.com.au
          </li>
        </ul>
      </div>
    </div>
  </section>

</main>
</body>
</html>
```